MLD Illustration Web Design

Create illustration web design company for Mandirasa Luhur Digital (MLD). I more prefer design with illustration concept. Detail for requirement please see attach file. I'm also attach MLD logo. This logo had 2 type, 2D design and 3D design. You can chose one of them, or used both.
For the winner or had good design would be possible to private project to completeness this website
Attach file requirement is guidance for design, but any changes are welcome
Updates
Sorry, I forgot about contact. Please add menu contact. You can put this menu besides login menu or part of menu level #1, or put on some where to adjust your design. Menu contact will give pop up window to email MLD Company and Company Information (Address, Telephone, etc)
Target Market(s)
Company (Business To Business)
Industry/Entity Type
It Company
Look and feel
Each slider illustrates characteristics of the customer's brand and the style your logo design should communicate.

```html
<!DOCTYPE html>
<html lang="en">
<head>
<meta charset="utf-8">
<title>MLD – Mobile Application</title>
<link href="https://fonts.googleapis.com/css2?family=Arimo:wght@400;700&display=swap" rel="stylesheet">
<style>
:root{
  --navy:#0b6a9a;
  --navy-dark:#075a84;
  --leaf:#7aa83a;
  --leaf-bright:#8cc63f;
  --sky-top:#7fd3ec;
  --sky-bottom:#b4e8f4;
  --grass-light:#c6f27a;
  --grass-mid:#8dd33a;
  --footer-top:#5f9e17;
  --footer-bottom:#69a81c;
  --footer-bar:#4d870f;
  --ink:#555;
  --link:#0b6a9a;
  --white:#fff;
}
*{margin:0;padding:0;box-sizing:border-box}
html,body{width:1200px;height:1050px;overflow:hidden}
body{position:relative;font-family:"Arimo",Arial,sans-serif;background:var(--footer-top);color:var(--ink)}
.scene{position:absolute;left:0;top:0;width:1200px;height:692px;background:linear-gradient(to bottom,var(--sky-top),var(--sky-bottom))}
.meadow{position:absolute;left:0;top:692px;width:1200px;height:84px;background:linear-gradient(to bottom,var(--grass-mid),var(--grass-light) 40%,var(--grass-mid))}
.top-strip{position:absolute;left:0;top:0;width:1200px;height:7px;background:var(--navy)}
.account-tab{position:absolute;left:757px;top:0;width:277px;height:35px;background:var(--navy);border-radius:0 0 14px 14px;display:flex;align-items:center;justify-content:center}
.account-tab a{color:var(--white);font-weight:700;font-size:14px;text-decoration:none;padding:0 19px}
.account-tab a+a{border-left:1px dotted rgba(255,255,255,.5)}
.brand{position:absolute;left:162px;top:30px;display:flex;align-items:center;gap:12px}
.brand-dot{width:56px;height:56px;border-radius:50%;background:var(--navy)}
.brand-name{font-size:56px;font-weight:700;color:var(--leaf);letter-spacing:2px;line-height:1}
.panel{position:absolute;left:138px;top:174px;width:811px;height:544px;background:var(--white);border-radius:4px;box-shadow:0 0 8px rgba(0,0,0,.18)}
.panel h1{position:absolute;left:35px;top:40px;font-size:26px;color:var(--leaf);font-weight:700}
.copy{position:absolute;left:34px;top:84px;width:322px;font-size:12px;line-height:16.6px;z-index:1}
.copy p{margin-bottom:16.6px}
.copy a{color:var(--link);text-decoration:none}
.ticks{list-style:none;margin-top:20px}
.ticks li{position:relative;padding-left:14px;line-height:22px}
.ticks li::before{content:"";position:absolute;left:2px;top:8px;border-left:4px solid var(--navy);border-top:3px solid transparent;border-bottom:3px solid transparent}
.hero-art{position:absolute;left:372px;top:66px;width:414px;height:429px;border-radius:30px;background:radial-gradient(ellipse at 55% 55%,#2a7fe0,#6bc3ee 45%,#f3f6f8 75%)}
.pager{position:absolute;left:372px;top:507px;display:flex;gap:6px}
.pager span{width:17px;height:17px;border-radius:50%;background:var(--navy)}
.pager .on{background:var(--white);border:5px solid var(--leaf)}
.main-nav{position:absolute;left:958px;top:179px;list-style:none}
.main-nav li{width:103px;height:30px;margin-bottom:8px;background:var(--navy);color:var(--white);font-weight:700;font-size:14px;display:flex;align-items:center;justify-content:center;border:1px solid #fff3}
.main-nav li.current{background:var(--leaf)}
.footer{position:absolute;left:0;top:776px;width:1200px;height:230px;background:linear-gradient(to bottom,var(--footer-top),var(--footer-bottom))}
.col{position:absolute;top:62px;width:140px;color:var(--white);font-size:11.5px}
.col h2{font-size:13px;font-weight:700;padding-bottom:4px;border-bottom:1px dotted #cde6a6;margin-bottom:18px}
.col li{list-style:none;line-height:16.6px}
.col-links{left:211px}
.col-cats{left:522px}
.col-social{left:828px;top:59px;width:152px}
.col-social li{display:flex;align-items:center;gap:10px;height:28px;border-bottom:1px solid #7bb63a}
.col-social li:last-child{border:0}
.col-social h2{margin-bottom:10px}
.sq{width:18px;height:18px;border-radius:2px}
.sq-blog{background:#f07c28}
.sq-circle{background:#3b5998}
.sq-work{background:#1177b5}
.sq-chirp{background:#5ec3ec}
.footer-bar{position:absolute;left:0;top:1006px;width:1200px;height:44px;background:var(--footer-bar);color:var(--white);font-size:11.5px;display:flex;align-items:center;justify-content:center}
</style>
</head>
<body>
<div class="scene" role="img" aria-label="Illustrated sky with white clouds and a row of trees on the horizon"></div>
<div class="meadow" role="img" aria-label="Illustrated grass meadow"></div>
<div class="top-strip"></div>
<nav class="account-tab"><a href="#">Sign In</a><a href="#">Register Now!</a></nav>
<div class="brand"><span class="brand-dot"></span><span class="brand-name">MLD</span></div>

<section class="panel">
  <h1>Mobile Application</h1>
  <div class="hero-art" role="img" aria-label="Illustration of a tablet with colourful app icons floating above its screen"></div>
  <div class="copy">
    <p>Lorem ipsum dolor sit amet. Sed do eiusmod tempoLorem ipsum dolor sit amet, consectetur <a href="#">adipisicing elit, sed do eiusmod tempor incididunt</a> at labore et dolore magna aliqua.</p>
    <p>Ut enim ad minim veniam, quis nostrud exercitation ullamco laboris nisi ut aliquip ex ea commodo consequat.</p>
    <p>Duis aute irure dolor <a href="#">in reprehenderit in voluptate</a> velit esse cillum dolore eu fugiat nulla pariatur. Excepteur sint occaecat cupidatat non proident.</p>
    <ul class="ticks">
      <li>Sed do eiusmod tempo</li>
      <li>Lorem ipsum dolor sit amet consectetur</li>
      <li>Adipisicing elit,</li>
      <li>Red do eiusmod tempor incididunt</li>
      <li>Ut labore et dolore magna</li>
    </ul>
  </div>
  <div class="pager"><span class="on"></span><span></span><span></span><span></span></div>
</section>

<ul class="main-nav">
  <li>Home</li>
  <li class="current">SERVICES</li>
  <li>Product</li>
  <li>Clients</li>
  <li>Company</li>
  <li>Blog</li>
</ul>

<footer class="footer">
  <div class="col col-links">
    <h2>USEFUL LINKS</h2>
    <ul><li>Home</li><li>Products</li><li>Accessories</li><li>Our Story</li><li>Questions</li><li>Blog</li><li>Where We Are</li></ul>
  </div>
  <div class="col col-cats">
    <h2>CATEGORIES</h2>
    <ul><li>LInk-1</li><li>LInk-1</li><li>LInk-1</li><li>LInk-1</li><li>LInk-1</li><li>LInk-1</li><li>LInk-1</li></ul>
  </div>
  <div class="col col-social">
    <h2>SOCIAL NETWORK</h2>
    <ul>
      <li><span class="sq sq-blog"></span>Bolg : @mld</li>
      <li><span class="sq sq-circle"></span>Join us on Circlepage</li>
      <li><span class="sq sq-work"></span>Join us on Worknet</li>
      <li><span class="sq sq-chirp"></span>Chirper : @mld</li>
    </ul>
  </div>
</footer>
<div class="footer-bar">© 2007–2013, mldigital.net. All Rights Reserved</div>
</body>
</html>
```